2in1 Bartender & Sommelier needs a business card

I need a business card. I worked as a bartender in many places but I just finished a sommelier school and I would like a new business card. I like minimal design, natural materials and something what makes the people think :) I try to be creative in cocktail making, like little mixology, little twist on recipes... I like to travel and discover new places, cultures and of course interesting drinks and improve continously...live a little bit crazy life. And I like what I do...

Target Market(s)

restaurant/winebar managers, winemakers, other sommeliers and bartenders, people who work in food and beverage sector

Industry/Entity Type

Hospitality

Contact Information for Business Card

Réka Fodor
Bartender & Sommelier
Phone: (FR) +33 6 4720 3917
(HU) +36 70 518 6092

Font styles to use
Script

Requirements
Must have
• Some sign, I am a bartender and sommelier as well.
Nice to have
• black and white maybe with 1 or 2 extra color
Should not have
• very colourful, to many things on the card

```html
<!DOCTYPE html>
<html lang="en">
<head>
<meta charset="utf-8">
<title>Réka Fodor – Bartender &amp; Sommelier business card</title>
<link rel="stylesheet" href="https://fonts.googleapis.com/css2?family=Jura:wght@500;600&family=Arimo:wght@400&display=swap">
<style>
  :root {
    --stage: #2a2a2a;
    --card-black: #1b1b1b;
    --card-black-edge: #2c2c2c;
    --card-white: #ffffff;
    --silver: #c9c9c9;
    --ink: #141414;
    --accent-orange: #c4531f;
    --accent-red: #d41f26;
    --divider: #9a9a9a;
    --contact: #222222;
  }
  * { box-sizing: border-box; margin: 0; padding: 0; }
  html, body {
    width: 1200px; height: 852px; overflow: hidden;
    background: var(--stage);
  }
  .stage {
    position: relative; width: 1200px; height: 852px;
    display: flex; align-items: center; justify-content: center; gap: 40px;
  }
  .card {
    position: relative; width: 520px; height: 297px;
    border-radius: 18px;
    box-shadow: 0 14px 30px rgba(0,0,0,.45);
  }
  /* Back side */
  .card-back {
    background: linear-gradient(160deg, var(--card-black-edge), var(--card-black) 60%);
    display: flex; align-items: center; justify-content: center; gap: 22px;
  }
  .back-mark {
    display: flex; align-items: center; gap: 12px;
    font-family: "Jura", sans-serif; font-weight: 600;
    font-size: 30px; color: var(--silver); letter-spacing: .5px;
  }
  .mark-dot {
    width: 14px; height: 14px; border-radius: 50%; background: var(--silver);
  }
  .back-rule { width: 2px; height: 44px; background: #555; }
  .back-initials {
    font-family: "Jura", sans-serif; font-weight: 600;
    font-size: 40px; color: var(--silver); letter-spacing: 2px;
  }
  /* Front side */
  .card-front {
    background: var(--card-white);
    padding: 0 26px 0 34px;
    display: flex; align-items: center;
  }
  .identity { display: flex; flex-direction: column; gap: 4px; }
  .identity-name {
    font-family: "Jura", sans-serif; font-weight: 600;
    font-size: 25px; color: var(--ink); letter-spacing: .5px;
  }
  .identity-role {
    font-family: "Arimo", sans-serif; font-size: 12px;
    color: var(--accent-orange);
  }
  .front-divider {
    width: 1px; height: 62px; background: var(--divider); margin: 0 12px 0 14px;
  }
  .contact-list {
    list-style: none; font-family: "Arimo", sans-serif;
    font-size: 11px; line-height: 1.7; color: var(--contact);
  }
  .front-mark {
    margin-left: auto; font-family: "Jura", sans-serif; font-weight: 600;
    font-size: 16px; color: var(--accent-red); text-align: right;
    align-self: center;
  }
</style>
</head>
<body>
  <main class="stage">
    <section class="card card-back" aria-label="Card back">
      <div class="back-mark"><span class="mark-dot"></span>Réka Fodor</div>
      <span class="back-rule"></span>
      <span class="back-initials">RF</span>
    </section>

    <section class="card card-front" aria-label="Card front">
      <div class="identity">
        <h1 class="identity-name">Réka Fodor</h1>
        <p class="identity-role">Bartender &amp; Sommelier</p>
      </div>
      <span class="front-divider"></span>
      <ul class="contact-list">
        <li>(FR) +33 6 4720 3917</li>
        <li>(HU) +36 70 518 6092</li>
        <li>E: reka.fodor84@cellarpost.com</li>
      </ul>
      <div class="front-mark">Réka Fodor</div>
    </section>
  </main>
</body>
</html>
```